Unique Home Cooking School needs Wordpress Design

We need a wordpress design for our small business based in Singapore called Brisk Ladles. It is a unique cooking school where the cooking course menu is completely customised to our client's preference/lifestyle/requests. More information can be found on our site: briskladles.example

We are looking for something simple and easy to navigate. We are currently using a free template which we have customised ourselves. As the business is growing, we are looking to have a site more suited to our needs. The site should also be photo friendly, as we often post up photos of our food. It should also be social media integrated as a lot of our business is driven by PQ.

The look and feel should really reflect the personalities of both owners - like the logo. Please feel free to contact us if you need more clarification.

Target Market(s)

Our target audience are usually female, with children, aged 25 - 45.
They are either stay-at-home mums or full-time mums that are keen to do more for the family.

Industry/Entity Type

Small Business

Requirements
Must have
• The wordpress design has to be able to accommodate food photos on every page.
It also needs to be able to support social media feeds within the site.
Should not have
• Design should not have any chef-like design elements as we are not chefs. We are two stay-home-mums wanting to impart skills to other stay-home-mums or domestic helpers.

```html
<!DOCTYPE html>
<html lang="en">
<head>
<meta charset="utf-8">
<title>Brisk Ladles – Home Cooking School</title>
<link rel="stylesheet" href="https://fonts.googleapis.com/css2?family=Questrial&family=Comfortaa:wght@400;700&display=swap">
<style>
:root{
  --ink:#1f1f1f;
  --muted:#3a3a3a;
  --link:#2b7bd0;
  --brown:#5b2f14;
  --soft:#f3f3f3;
  --rule:#9a9a9a;
  --footer:#1b1b1b;
  --footer-text:#ffffff;
  --accent:#e07b1c;
  --white:#ffffff;
}
*{box-sizing:border-box;margin:0;padding:0}
html,body{width:1200px;height:2827px;overflow:hidden}
body{position:relative;background:var(--white);font-family:"Questrial",sans-serif;color:var(--ink)}
.abs{position:absolute}
.art{position:absolute;border-radius:6px}

/* hero + header */
.hero{left:0;top:0;width:1200px;height:722px;
  background:linear-gradient(115deg,#d9d5cf 0%,#f1ede6 25%,#e8c9b2 45%,#f5f1ec 60%,#d8b49a 78%,#c9a184 100%)}
.hero-food{left:0;top:520px;width:1200px;height:202px;
  background:linear-gradient(90deg,#b8c54a 0%,#e0a23a 18%,#d7442a 40%,#f2ece2 55%,#cc3b24 72%,#a7b84c 90%,#d6c2a8 100%);opacity:.85}
.site-header{left:0;top:0;width:1200px;height:214px;background:rgba(255,255,255,.88)}
.brand{left:88px;top:25px;width:232px;height:182px;background:var(--white);display:flex;flex-direction:column;align-items:center;justify-content:center;gap:10px}
.brand-dot{width:70px;height:70px;border-radius:50%;background:var(--accent)}
.brand-name{font-family:"Comfortaa",sans-serif;font-weight:700;font-size:26px;color:var(--brown)}
.brand-tag{font-size:11px;color:var(--muted)}
.nav{left:432px;top:110px;display:flex;gap:40px;font-size:14px;color:var(--ink)}
.hero-title{left:270px;top:425px;width:680px;height:66px;background:rgba(255,255,255,.82);display:flex;align-items:center;justify-content:center;font-family:"Comfortaa",sans-serif;font-size:28px;white-space:nowrap;color:var(--ink)}
.hero-sub{left:340px;top:512px;width:520px;height:46px;background:rgba(255,255,255,.82);display:flex;align-items:center;justify-content:center;font-size:22px;white-space:nowrap}

/* shared type */
.heading{font-family:"Comfortaa",sans-serif;font-size:27px;color:var(--ink)}
.copy{font-size:13.5px;line-height:25px;color:var(--muted)}
.read-more{font-size:14px;color:var(--link)}

.services{left:0;top:1146px;width:1200px;height:424px;background:var(--soft)}
.divider{left:0;top:1866px;width:1200px;height:2px;background:var(--rule)}

.bullets{list-style:none}
.bullets li{font-size:14px;line-height:28px;color:var(--ink);padding-left:20px;position:relative}
.bullets li::before{content:"";position:absolute;left:2px;top:12px;width:6px;height:6px;border-radius:50%;background:var(--ink)}
.btn{width:245px;height:50px;background:var(--brown);color:var(--white);display:flex;align-items:center;justify-content:center;font-size:18px}

/* footer */
.site-footer{left:0;top:2340px;width:1200px;height:487px;background:var(--footer);color:var(--footer-text)}
.f-col{position:absolute;top:44px}
.f-col h3{font-family:"Comfortaa",sans-serif;font-size:20px;font-weight:700;margin-bottom:12px}
.f-col li{list-style:none;font-size:12.5px;line-height:21px}
.f-post{font-size:12.5px;line-height:21px}
.f-post .more{color:var(--accent)}
.socials{position:absolute;left:506px;top:218px;display:flex;gap:18px}
.socials span{width:38px;height:38px;border-radius:50%;background:var(--white);display:block}
.legal{position:absolute;left:0;top:300px;width:1200px;text-align:center;font-size:12.5px;line-height:24px}
</style>
</head>
<body>

<div class="abs hero" role="img" aria-label="Photo of a mother and child cooking together in a bright kitchen"></div>
<div class="abs hero-food" role="img" aria-label="Fresh vegetables and fruit on the kitchen counter"></div>

<header class="abs site-header">
  <div class="abs brand">
    <span class="brand-dot"></span>
    <span class="brand-name">Brisk Ladles</span>
    <span class="brand-tag">Cooking lessons for everyone</span>
  </div>
  <nav class="abs nav">
    <span>Home</span><span>About Us</span><span>Our Services</span><span>Training</span><span>News</span><span>Blogs</span><span>Contact Us</span>
  </nav>
</header>

<div class="abs hero-title">Lorem Ipsum is simply dummy text of the</div>
<div class="abs hero-sub">Lorem Ipsum is simply dummy text of the</div>

<section>
  <div class="art" style="left:126px;top:790px;width:345px;height:320px;background:linear-gradient(160deg,#f6e3cf,#e9a86b 55%,#c94a2a)" role="img" aria-label="Illustration of a mum cooking at the stove"></div>
  <h2 class="abs heading" style="left:640px;top:800px">Lorem Ipsum is simply</h2>
  <p class="abs copy" style="left:518px;top:845px;width:648px;text-align:center">Lorem Ipsum is simply dummy text of the printing and typesetting industry. Lorem Ipsum has been the industry's standard dummy text ever since the 1500s, when an unknown printer took a galley of type and scrambled it to make a type specimen book. It has survived not only five centuries, but also the leap into electronic typesetting, remaining essentially unchanged. It was popularised in the 1960s with the release of Letraset sheets containing</p>
  <a class="abs read-more" style="left:750px;top:1066px">Read More</a>
</section>

<section class="abs services">
  <h2 class="abs heading" style="left:238px;top:50px">Our Services</h2>
  <p class="abs copy" style="left:120px;top:95px;width:425px;text-align:center">Lorem Ipsum is simply dummy text of the printing and typesetting industry. Lorem Ipsum has been the industry's standard dummy text ever since the 1500s, when an unknown printer took a galley of type and scrambled it to make a type specimen book. It has survived not only five centuries, but also the leap into electronic typesetting, remaining essentially unchanged.</p>
  <a class="abs read-more" style="left:314px;top:312px">Read More</a>
  <div class="art" style="left:630px;top:22px;width:500px;height:380px;background:linear-gradient(135deg,#f7f3ee,#c98a4a 45%,#3a3a3a 75%,#f7f3ee)" role="img" aria-label="Illustration of a family at a dining table being served"></div>
</section>

<section>
  <div class="art" style="left:266px;top:1640px;width:190px;height:182px;background:linear-gradient(150deg,#f4e9dc,#6aa1c9 50%,#d9442c)" role="img" aria-label="Illustration of a cook holding a plate of food"></div>
  <h2 class="abs heading" style="left:470px;top:1638px">Best Food At Home</h2>
  <p class="abs copy" style="left:470px;top:1680px;width:700px">Lorem Ipsum is simply dummy text of the printing and typesetting industry. Lorem Ipsum has been the industry's standard dummy text ever since the 1500s, when an unknown printer took a galley of type and scrambled it to make a type specimen book. It has survived not only five centuries, but also the leap into electronic typesetting, remaining essentially unchanged.</p>
</section>

<div class="abs divider"></div>

<section>
  <h2 class="abs heading" style="left:100px;top:1940px">Lorem Ipsum is simply</h2>
  <ul class="abs bullets" style="left:100px;top:1998px">
    <li>Lorem Ipsum is simply dummy text of the</li>
    <li>Lorem Ipsum is simply dummy</li>
    <li>Lorem Ipsum is simply text of the</li>
    <li>Lorem Ipsum is simply dummy text of the</li>
    <li>Lorem Ipsum is simply</li>
    <li>Lorem Ipsum is simply dummy text</li>
  </ul>
  <a class="abs btn" style="left:100px;top:2217px">Find More Links</a>

  <div class="art" style="left:462px;top:1900px;width:280px;height:410px;background:linear-gradient(170deg,#f6efe6,#7c4a2a 30%,#9fc3d9 60%,#f6efe6)" role="img" aria-label="Illustration of a waitress carrying two plates"></div>

  <h2 class="abs heading" style="left:772px;top:1940px">Lorem Ipsum is simply</h2>
  <ul class="abs bullets" style="left:772px;top:1998px">
    <li>Lorem Ipsum is simply dummy text of the</li>
    <li>Lorem Ipsum is simply dummy</li>
    <li>Lorem Ipsum is simply text of the</li>
    <li>Lorem Ipsum is simply dummy text of the</li>
    <li>Lorem Ipsum is simply</li>
    <li>Lorem Ipsum is simply dummy text</li>
  </ul>
  <a class="abs btn" style="left:772px;top:2217px">Find More Links</a>
</section>

<footer class="abs site-footer">
  <div class="f-col" style="left:119px">
    <h3>Lorem Ipsum</h3>
    <ul><li>Lorem Ipsum is simply</li><li>Lorem Ipsum</li><li>Lorem Ipsum is simply</li><li>Lorem</li><li>Lorem Ipsum is simply</li></ul>
  </div>
  <div class="f-col" style="left:339px">
    <h3>Lorem</h3>
    <ul><li>Lorem Ipsum is simply</li><li>Lorem Ipsum is simply</li><li>Lorem Ipsum is simply</li><li>Lorem</li><li>Lorem Ipsum is simply</li><li>Lorem Ipsum is simply</li></ul>
  </div>
  <div class="f-col" style="left:590px">
    <h3>Brisk Ladles</h3>
    <ul><li>Home</li><li>Blog</li><li>What to Expect</li><li>About</li><li>Contact/Locations</li></ul>
  </div>
  <div class="f-col" style="left:870px;width:280px">
    <h3>Recent We blog Posts</h3>
    <p class="f-post">How The Brain Changes As We Age<br>As we age our brains change too.<br>Most peopl <span class="more">Read more...</span></p>
    <p class="f-post" style="margin-top:12px">How The Brain Changes As We Age<br>As we age our brains change too.<br>Most peopl <span class="more">Read more...</span></p>
  </div>
  <div class="socials" aria-label="Social links"><span></span><span></span><span></span><span></span></div>
  <div class="legal">
    <p>© 2011-2014 Brisk Ladles, All rights reserved</p>
    <p>Home / Blog / What to Expect / About / Contact/Locations / Services / Privacy Policy</p>
  </div>
</footer>

</body>
</html>
```